Harbor Crest Real Estate Business Cards

Looking to create a template for the agents in my office. The images below are an example of our current card, logos, and tagline. The requirements are:
1. Needs to include photo of agent
2. Needs to include Logo
3. Needs to include tag line. (current card doesn't include tagline.)
4. Needs to include phone, address, email, website and social media logos i.e. Find me at "f", "twitter (logo)" etc.
5. Need front and back design.
6. I don't want the old style safe style of business card. I want it to stand out in a stack of cards.
7. Do not make it look anything like what i currently have. This needs to be all new.
Thank you for your time.
Industry/Entity Type
Real Estate Agent
Contact Information for Business Card
I need name, address, email, website (www.pinevalleyhomefinder.example) social media logos
Requirements
Must have
- 1. Needs to include photo of agent
- 2. Needs to include Logo
- 3. Needs to include tag line. (current card doesn't include tagline.)
- 4. Needs to include phone, address, email, website and social media logos i.e. Find me at "f", "twitter (logo)" etc.
- 5. Need front and back design.
- 6. I don't want the old style safe style of business card. I want it to stand out in a stack of cards.
- 7. Do not make it look anything like what i currently have. This needs to be all new.
Should not have
- Not boring or plain.

```html
<!DOCTYPE html>
<html lang="en">
<head>
<meta charset="utf-8">
<title>Harbor Crest Real Estate – Business Cards</title>
<link rel="stylesheet" href="https://fonts.googleapis.com/css2?family=Open+Sans:wght@400;600;700;800&display=swap">
<style>
  :root {
    --backdrop: #2b2b2d;
    --card: #ffffff;
    --brand-red: #c8202f;
    --brand-grey: #5f5957;
    --ink: #333333;
    --photo-light: #e9e9ea;
    --photo-dark: #4a4a4e;
    --font: "Open Sans", Arial, sans-serif;
  }
  * { box-sizing: border-box; margin: 0; padding: 0; }
  html, body { width: 1200px; height: 900px; overflow: hidden; }
  body { background: var(--backdrop); font-family: var(--font); position: relative; }

  .card {
    position: absolute;
    left: 240px;
    width: 720px;
    height: 411px;
    background: var(--card);
    overflow: hidden;
  }
  .card--front { top: 28px; }
  .card--back { top: 461px; }

  .brand-name {
    font-family: var(--font);
    font-weight: 800;
    color: var(--brand-grey);
    letter-spacing: -0.5px;
    text-transform: uppercase;
    line-height: 1;
    white-space: nowrap;
  }
  .brand-sub {
    font-family: var(--font);
    font-weight: 800;
    color: var(--brand-grey);
    text-transform: uppercase;
    line-height: 1;
    white-space: nowrap;
  }
  .tagline {
    font-family: var(--font);
    font-weight: 400;
    color: var(--brand-grey);
    white-space: nowrap;
  }
  .tagline em { font-style: normal; color: var(--brand-red); }

  /* Front */
  .agent-photo {
    position: absolute;
    left: 28px;
    top: 30px;
    width: 300px;
    height: 381px;
    background: linear-gradient(180deg, var(--photo-light) 0%, #bdbdc0 35%, var(--photo-dark) 100%);
  }
  .card--front .brand {
    position: absolute;
    right: 40px;
    top: 80px;
    text-align: right;
  }
  .card--front .brand-name { font-size: 34px; }
  .card--front .brand-sub { font-size: 16px; letter-spacing: 4px; margin-top: 4px; }
  .card--front .tagline { font-size: 16px; margin-top: 10px; }

  .social {
    position: absolute;
    right: 50px;
    top: 285px;
  }
  .social__title {
    color: var(--brand-red);
    font-weight: 600;
    font-size: 19px;
    letter-spacing: 1px;
    margin-bottom: 10px;
  }
  .social__row {
    display: flex;
    align-items: center;
    gap: 12px;
    font-size: 18px;
    color: var(--ink);
    letter-spacing: 0.5px;
    margin-bottom: 4px;
  }
  .social__dot {
    width: 20px; height: 20px; border-radius: 50%;
    background: var(--brand-grey);
    flex: none;
  }

  /* Back */
  .card--back .brand {
    position: absolute;
    left: 0; right: 0;
    top: 78px;
    text-align: center;
  }
  .card--back .brand-name { font-size: 38px; }
  .card--back .brand-sub { font-size: 17px; letter-spacing: 5px; margin-top: 5px; }
  .card--back .tagline { font-size: 17px; margin-top: 12px; }

  .agent-id {
    position: absolute;
    right: 400px;
    top: 196px;
    text-align: right;
  }
  .agent-id__name {
    font-size: 32px;
    font-weight: 700;
    color: var(--brand-grey);
    letter-spacing: 1px;
    white-space: nowrap;
  }
  .agent-id__name span { color: var(--brand-red); }
  .agent-id__role {
    font-size: 20px;
    font-weight: 700;
    color: var(--brand-grey);
  }
  .divider {
    position: absolute;
    left: 338px;
    top: 198px;
    width: 2px;
    height: 78px;
    background: var(--brand-red);
  }
  .contacts {
    position: absolute;
    left: 362px;
    top: 194px;
    list-style: none;
  }
  .contacts li {
    display: flex;
    align-items: center;
    gap: 12px;
    font-size: 17px;
    color: var(--ink);
    letter-spacing: 0.3px;
    line-height: 27px;
    white-space: nowrap;
  }
  .contacts svg { width: 16px; height: 16px; flex: none; fill: var(--brand-red); }
  .contacts .web-accent { color: var(--brand-red); }
  .address {
    position: absolute;
    left: 0; right: 0;
    top: 300px;
    text-align: center;
    font-size: 19px;
    color: var(--ink);
  }
</style>
</head>
<body>

<section class="card card--front">
  <div class="agent-photo" role="img" aria-label="Portrait photo of the agent in a dark suit, arms crossed"></div>

  <div class="brand">
    <div class="brand-name">Harbor Crest</div>
    <div class="brand-sub">Real Estate</div>
    <div class="tagline">Your <em>Harbor.</em> Your <em>Home.</em> Your <em>Next Chapter.</em></div>
  </div>

  <div class="social">
    <div class="social__title">Follow us on:</div>
    <div class="social__row"><span class="social__dot"></span>/harborcrestre</div>
    <div class="social__row"><span class="social__dot"></span>/harborcrestre</div>
  </div>
</section>

<section class="card card--back">
  <div class="brand">
    <div class="brand-name">Harbor Crest</div>
    <div class="brand-sub">Real Estate</div>
    <div class="tagline">Your <em>Harbor.</em> Your <em>Home.</em> Your <em>Next Chapter.</em></div>
  </div>

  <div class="agent-id">
    <div class="agent-id__name">DANIEL <span>PRICE</span></div>
    <div class="agent-id__role">CEO/Founder</div>
  </div>

  <div class="divider"></div>

  <ul class="contacts">
    <li>
      <svg viewBox="0 0 24 24" aria-hidden="true"><path d="M6.6 10.8a15.1 15.1 0 0 0 6.6 6.6l2.2-2.2c.3-.3.7-.4 1-.2 1.1.4 2.3.6 3.6.6.6 0 1 .4 1 1V20c0 .6-.4 1-1 1A17 17 0 0 1 3 4c0-.6.4-1 1-1h3.5c.6 0 1 .4 1 1 0 1.3.2 2.5.6 3.6.1.3 0 .7-.2 1z"/></svg>
      (000)000 0000
    </li>
    <li>
      <svg viewBox="0 0 24 24" aria-hidden="true"><path d="M2 5h20v14H2z M3.5 6.5 12 13l8.5-6.5" fill="var(--brand-red)" stroke="#fff" stroke-width="1.4"/></svg>
      info@danielprice.example
    </li>
    <li>
      <svg viewBox="0 0 24 24" aria-hidden="true"><circle cx="12" cy="12" r="10"/><path d="M2 12h20M12 2c3 3 3 17 0 20M12 2c-3 3-3 17 0 20" fill="none" stroke="#fff" stroke-width="1.3"/></svg>
      <span>www.<span class="web-accent">pinevalleyhomefinder</span>.example</span>
    </li>
  </ul>

  <div class="address">Your Street Address, New York, 1234</div>
</section>

</body>
</html>
```